Yoga Workshop - Yoga Practice information flyer

I am a yoga teacher who will be presenting a workshop on yoga for sleep and need a brochure for my clients which outlines a practice that I give them so they can do the practice at home. Ideally I would like a brochure that is a single A3 size of paper in size that folds in half to an A4 booklet with the entire practice on the centre section to make it easy for people to do the practice at home with just one open page in front of them:
* Front page detailing "Yoga for Sleep Workshop" and "Restorative Yoga Practice"
* Centre contains the information on the practice contained in the attached word document. The practice consists of 5 postures, so there needs to be five separate sections which have the pictures of the postures (attached in uploaded files) and the wording contained in the attached word document. All pictures uploaded need to be included in the flyer as each posture has different pictures demonstrating the posture using yoga props or using things people have at home
* Back page containing a picture of myself (picture uploaded in files) with some information about me (contained in the attached word document) and my website www.lumaverisk.com.au

I also need this flyer to be able to printed on 2 double sided A4 sheets of paper so will require 2 x pdf file versions. Importantly, for the centre section of the flyer, the design needs to ensure if it is printed on A4 paper, the wording and pictures for each of the postures are not separated over two pages

Target Market(s)

Existing clients

Requirements
Must have
• Detailed in project description
Nice to have
• The word document also contains some quotes. These do not need to be included in the flyer. If there is room and there is room for one or two of those please include where it would look good
Should not have
• Stock pictures of people in yoga postures which a normal everyday person could not get into

```html
<!DOCTYPE html>
<html lang="en">
<head>
<meta charset="utf-8">
<title>Yoga for Sleep Workshop – Restorative Yoga Sleep Sequence</title>
<link rel="stylesheet" href="https://fonts.googleapis.com/css2?family=Fraunces:wght@600;700&family=Jost:ital,wght@0,300;0,400;0,500;0,600;1,300;1,600&display=swap">
<style>
  :root {
    --clay: #c67d5b;
    --clay-deep: #b9714f;
    --clay-light: #e9b59d;
    --blush: #f6e5dc;
    --blush-soft: #faf0ea;
    --navy: #2d3954;
    --ink: #3b3b3b;
    --paper: #ffffff;
    --backdrop: #ededed;
    --photo-wood: #8a5a3a;
    --photo-mat: #2d8fc4;
  }
  * { box-sizing: border-box; margin: 0; padding: 0; }
  html, body { width: 875px; height: 1200px; overflow: hidden; background: var(--backdrop); }
  body { position: relative; font-family: "Jost", sans-serif; color: var(--ink); }

  .page { position: absolute; width: 370px; height: 525px; background: var(--paper); overflow: hidden; }
  .page--back  { left: 68px;  top: 51px; }
  .page--cover { left: 438px; top: 51px; background: #fbfbfb; }
  .page--inner-left  { left: 68px;  top: 623px; }
  .page--inner-right { left: 438px; top: 623px; background: #fbfbfb; }

  .abs { position: absolute; }
  .serif { font-family: "Fraunces", serif; font-weight: 700; }

  /* back page */
  .eyebrow { font-size: 7.5px; color: var(--ink); }
  .eyebrow::after { content: ""; display: inline-block; width: 20px; height: 1px; background: var(--ink); margin-left: 4px; vertical-align: middle; }
  .teacher-name { font-size: 17px; color: var(--clay); letter-spacing: -0.2px; }
  .teacher-bio { font-size: 8px; line-height: 12.4px; width: 140px; font-weight: 300; color: #333; }

  .quote-mark { width: 32px; height: 32px; border-radius: 50%; background: linear-gradient(135deg, var(--clay-light), var(--clay)); color: #fff; font-family: "Fraunces", serif; font-size: 26px; line-height: 40px; text-align: center; }
  .quote-text { font-size: 13px; line-height: 17px; font-weight: 300; font-style: italic; color: var(--navy); }
  .quote-text b { font-weight: 600; }
  .quote-source { font-size: 9.5px; color: var(--clay); font-family: "Fraunces", serif; font-weight: 600; }
  .quote-source::before { content: ""; display: inline-block; width: 14px; height: 1px; background: var(--navy); margin-right: 5px; vertical-align: middle; }

  .studio-name { font-family: "Jost", sans-serif; font-weight: 500; color: var(--navy); letter-spacing: 0.3px; }
  .studio-dot { width: 30px; height: 30px; border-radius: 50%; border: 1.5px solid var(--clay); }
  .studio-tagline { font-size: 4.6px; color: var(--navy); }
  .website { font-size: 8.5px; color: var(--navy); }

  /* cover */
  .cover-tagline { font-size: 6.6px; letter-spacing: 1.1px; color: var(--navy); width: 370px; text-align: center; }
  .cover-heading { width: 370px; text-align: center; color: #fff; font-family: "Fraunces", serif; font-weight: 700; }
  .cover-copy { width: 236px; left: 67px; text-align: center; color: #fff; font-size: 7.6px; line-height: 11.3px; font-weight: 300; }

  /* inner spread */
  .posture-label { font-size: 7.5px; color: var(--ink); }
  .posture-title { font-size: 11.4px; color: var(--clay); line-height: 14.5px; letter-spacing: -0.2px; }
  .photo { position: absolute; border-radius: 9px; overflow: hidden; }
  .photo--floor { background: linear-gradient(160deg, #a06a45 0%, var(--photo-wood) 35%, var(--photo-mat) 55%, #6e4530 100%); }
  .photo--props { background: linear-gradient(170deg, #7a4c31 0%, #c1693a 55%, #6a3f2b 100%); }
  .photo--wall  { background: linear-gradient(180deg, #e7e7e5 0%, #d9d6d2 45%, #8a5a3a 60%, var(--photo-mat) 80%); }
  .photo-tag { position: absolute; left: 0; bottom: 0; padding: 1px 8px 1px 7px; background: var(--clay-light); color: #fff; font-size: 4px; border-top-right-radius: 5px; }

  .section-head { font-size: 6.6px; color: var(--clay); font-weight: 600; }
  .section-body { font-size: 6.2px; line-height: 9.8px; font-weight: 300; color: #333; }
  .section-body ul { list-style: none; }
  .section-body li { padding-left: 8px; position: relative; }
  .section-body li::before { content: "•"; position: absolute; left: 1px; }

  .closing-band { left: 0; top: 484px; width: 354px; height: 41px; background: linear-gradient(90deg, #ddab93, var(--clay)); border-top-right-radius: 22px; }
  .closing-band p { position: absolute; left: 26px; top: 12px; color: #fff; font-size: 10px; font-style: italic; font-weight: 300; white-space: nowrap; }
</style>
</head>
<body>

<!-- Back page: about the teacher -->
<section class="page page--back">
  <svg class="abs" style="left:0;top:0" width="370" height="525" viewBox="0 0 370 525">
    <rect x="167" y="38" width="9" height="9" fill="var(--clay-light)"/>
    <rect x="167" y="58" width="9" height="9" fill="var(--clay-light)"/>
    <circle cx="192" cy="82" r="7.5" fill="none" stroke="var(--clay-light)" stroke-width="3.5"/>
    <path d="M262 53 C298 92 361 135 361 195 C361 245 322 276 262 276 C202 276 163 245 163 195 C163 135 226 92 262 53Z" fill="none" stroke="var(--clay-light)" stroke-width="0.8"/>
    <path d="M262 63 C296 100 355 140 355 196 C355 243 318 273 262 273 C206 273 169 243 169 196 C169 140 228 100 262 63Z" fill="var(--clay)"/>
  </svg>
  <svg class="abs" style="left:0;top:0" width="370" height="525" viewBox="0 0 370 525" role="img" aria-label="Photo of the teacher sitting cross-legged in meditation on grass">
    <defs>
      <linearGradient id="teacherPhoto" x1="0" y1="0" x2="0" y2="1">
        <stop offset="0" stop-color="#9aa56a"/>
        <stop offset="0.5" stop-color="#6f7c49"/>
        <stop offset="1" stop-color="#a3956c"/>
      </linearGradient>
    </defs>
    <path d="M262 84 C292 115 349 150 349 198 C349 240 316 265 262 265 C208 265 175 240 175 198 C175 150 232 115 262 84Z" fill="url(#teacherPhoto)"/>
  </svg>

  <p class="abs eyebrow" style="left:23px;top:80px">About the teacher</p>
  <h2 class="abs serif teacher-name" style="left:23px;top:93px">Mara Ellison</h2>
  <p class="abs teacher-bio" style="left:23px;top:120px">Mara Ellison is a current serving Naval Officer, Yoga Therapist (C-YTC) and DeepRest Level 2 instructor. Mara’s classes are about using the practices and teaching of Yoga to come to the essence of your true self and learning to tap into the internal wisdom which is always present. Mara is dedicated to making the resilience developing practices of Yoga accessible to all Australian Military personnel and their families.</p>

  <div class="abs quote-mark" style="left:29px;top:309px">”</div>
  <p class="abs quote-text" style="left:72px;top:310px">Posture should be <b>steady<br>and comfortable</b></p>
  <p class="abs quote-source" style="left:73px;top:347px">Yoga Sutras of Aravinda</p>

  <div class="abs quote-mark" style="left:156px;top:389px">”</div>
  <p class="abs quote-text" style="left:199px;top:390px"><b>Life isn’t as serious</b> as<br>the mind makes it out to be</p>
  <p class="abs quote-source" style="left:199px;top:427px">Elias Torrin</p>

  <div class="abs studio-dot" style="left:32px;top:469px"></div>
  <p class="abs studio-name" style="left:76px;top:471px;font-size:14px">Stillhaven Studio</p>
  <p class="abs studio-tagline" style="left:77px;top:491px">Rest is where the change begins</p>
  <p class="abs website" style="left:256px;top:478px">www.lumaverisk.com.au</p>
</section>

<!-- Front cover -->
<section class="page page--cover">
  <svg class="abs" style="left:0;top:0" width="370" height="525" viewBox="0 0 370 525">
    <defs>
      <linearGradient id="coverDrop" x1="0" y1="0" x2="0" y2="1">
        <stop offset="0" stop-color="#edbfa9"/>
        <stop offset="0.6" stop-color="#d68e6c"/>
        <stop offset="1" stop-color="var(--clay-deep)"/>
      </linearGradient>
    </defs>
    <path d="M188 123 C235 185 370 255 370 400 L370 525 L0 525 L0 400 C0 255 141 185 188 123Z" fill="var(--blush-soft)"/>
    <path d="M188 150 C232 205 362 275 362 405 L362 525 L14 525 L14 405 C14 275 144 205 188 150Z" fill="var(--blush)"/>
    <path d="M188 174 C228 228 349 300 349 405 C349 465 322 505 300 525 L76 525 C54 505 27 465 27 405 C27 300 148 228 188 174Z" fill="url(#coverDrop)"/>
    <path d="M188 177 L140 238 M188 177 L236 238" stroke="#fff" stroke-width="1.2" fill="none"/>
    <line x1="157" y1="309" x2="183" y2="309" stroke="#fff" stroke-width="0.9"/>
    <circle cx="188" cy="309" r="2.4" fill="none" stroke="#fff" stroke-width="0.9"/>
    <line x1="193" y1="309" x2="219" y2="309" stroke="#fff" stroke-width="0.9"/>
    <rect x="148" y="308" width="3" height="1" fill="#fff"/><rect x="225" y="308" width="3" height="1" fill="#fff"/>
    <rect x="66" y="322" width="9" height="9" fill="#fff" opacity="0.45"/>
    <rect x="66" y="342" width="9" height="9" fill="#fff" opacity="0.45"/>
    <circle cx="90" cy="364" r="7" fill="none" stroke="#fff" stroke-opacity="0.45" stroke-width="3"/>
    <rect x="297" y="322" width="9" height="9" fill="#fff" opacity="0.45"/>
    <rect x="297" y="342" width="9" height="9" fill="#fff" opacity="0.45"/>
    <circle cx="284" cy="364" r="7" fill="none" stroke="#fff" stroke-opacity="0.45" stroke-width="3"/>
    <circle cx="188" cy="58" r="15" fill="none" stroke="var(--clay)" stroke-width="1.5"/>
  </svg>
  <p class="abs studio-name" style="left:0;top:82px;width:370px;text-align:center;font-size:18px">Stillhaven Studio</p>
  <p class="abs cover-tagline" style="left:0;top:111px">Rest is where the change begins</p>

  <h1 class="abs cover-heading" style="left:0;top:241px;font-size:19px;line-height:26px">Yoga for<br>Sleep Workshop</h1>
  <h2 class="abs cover-heading" style="left:0;top:324px;font-size:18.5px;line-height:26px">Restorative Yoga<br>Sleep Sequence</h2>
  <p class="abs cover-copy" style="top:390px">Use this sequence to relax and unwind at the end of a day or before bed. Settle comfortably into each posture for about 5-7 minutes. Set a timer to let you know when it is time to change position, and you can also listen to any music you find relaxing at the same time. The audio recording from the Yoga for Sleep Workshop can also be used to recreate the practice at home.</p>
  <p class="abs cover-copy" style="top:467px">In the middle of the night when you can’t sleep, you might like to try getting up and resting in any one of these postures for about 5-10 minutes before heading back to bed.</p>
</section>

<!-- Inner spread, left: postures 1 and 2 -->
<section class="page page--inner-left">
  <p class="abs posture-label" style="left:25px;top:26px">Posture 1</p>
  <h3 class="abs serif posture-title" style="left:25px;top:37px">Supported Chest Opening with Knee Support</h3>
  <div class="photo photo--floor" style="left:25px;top:63px;width:96px;height:134px" role="img" aria-label="Photo of a woman lying back on a lengthways bolster with a rolled towel under the knees"></div>
  <div class="photo photo--props" style="left:133px;top:63px;width:92px;height:36px" role="img" aria-label="Photo of the bolster props for the posture"><span class="photo-tag">Props</span></div>
  <div class="photo photo--floor" style="left:133px;top:106px;width:92px;height:90px" role="img" aria-label="Photo of the T-shaped bolster setup on the mat"><span class="photo-tag">Set up</span></div>
  <p class="abs section-head" style="left:238px;top:62px">Props</p>
  <div class="abs section-body" style="left:238px;top:72px;width:118px"><ul><li>2 x bolsters (or towels rolled up lengthways)</li><li>1 x cushion for head support (optional)</li></ul></div>
  <p class="abs section-head" style="left:238px;top:114px">Set up notes</p>
  <p class="abs section-body" style="left:238px;top:124px;width:118px">Position the props in a T-position with one bolster/towel running parallel to the yoga mat and one bolster towel running horizontal to the mat underneath the knees. Position yourself so your buttocks is on the floor and the parallel bolster runs from the lower back up to behind the head.</p>
  <p class="abs section-head" style="left:25px;top:206px">Caution</p>
  <p class="abs section-body" style="left:25px;top:216px;width:290px">If any lower back pain is experience adjust the parallel bolster height by using a towel. If using a towel, the height of the parallel support prop can be adjusted by either using a thinner towel or loosely rolling the towel. Do not us any parallel support prop if pain continues.</p>

  <p class="abs posture-label" style="left:25px;top:258px">Posture 2</p>
  <h3 class="abs serif posture-title" style="left:25px;top:269px">Supported Bound-Angle Pose</h3>
  <div class="photo photo--floor" style="left:25px;top:294px;width:96px;height:133px" role="img" aria-label="Photo of a woman reclining with soles together and knees supported by pillows"></div>
  <div class="photo photo--floor" style="left:133px;top:294px;width:96px;height:133px" role="img" aria-label="Photo of a woman reclining with soles together and knees supported by blocks"><span class="photo-tag">Props</span></div>
  <p class="abs section-head" style="left:238px;top:303px">Props</p>
  <div class="abs section-body" style="left:238px;top:313px;width:124px"><ul><li>1 x bolsters (or towel rolled up lengthways)</li><li>2 x yoga blocks/bolsters (or pillows)</li><li>1 x cushion for head support (optional)</li></ul></div>
  <p class="abs section-head" style="left:238px;top:354px">Set up notes</p>
  <p class="abs section-body" style="left:238px;top:364px;width:110px">Similar to Posture 1 without the bolster behind the knees. Instead, the soles of the feet are together with knees wide being supported by either blocks, bolsters or pillows</p>
  <p class="abs section-head" style="left:25px;top:437px">Caution</p>
  <p class="abs section-body" style="left:25px;top:447px;width:290px">If any lower back pain is experience adjust the parallel bolster height by using a towel. If using a towel, the height of the parallel support prop can be adjusted by either using a thinner towel or loosely rolling the towel. Do not us any parallel support prop if pain continues.</p>

  <div class="abs closing-band"><p>Tension is who you think you are, Relaxation is who you actually are</p></div>
</section>

<!-- Inner spread, right: postures 3, 4 and 5 -->
<section class="page page--inner-right">
  <p class="abs posture-label" style="left:16px;top:26px">Posture 3</p>
  <h3 class="abs serif posture-title" style="left:16px;top:37px">Elevated Legs-Up-the-Wall Pose</h3>
  <div class="photo photo--wall" style="left:16px;top:63px;width:96px;height:143px" role="img" aria-label="Photo of a woman lying with legs up the wall and hips on a bolster"></div>
  <div class="photo photo--props" style="left:123px;top:63px;width:97px;height:36px" role="img" aria-label="Photo of the bolster under the hips"><span class="photo-tag">Props</span></div>
  <p class="abs section-head" style="left:228px;top:61px">Props</p>
  <div class="abs section-body" style="left:228px;top:71px;width:125px"><ul><li>1 x bolsters (or towel or blanket densely folded to a width of about 15-30cm)</li><li>1 x cushion for head support (optional)</li></ul></div>
  <p class="abs section-head" style="left:124px;top:105px">Set up notes</p>
  <p class="abs section-body" style="left:124px;top:115px;width:228px">To enter the posture sit at 90 degrees to the wall with the side of your hip about a hand width away from the wall, and the bolster/folded towel or blanket close by. Lie down on the mat on your side then roll onto your back and extend feet up wall. The feet can push into the wall to elevate the hips slightly so the bolster/folded towel or blanket can slide underneath the hips. The prop should be positioned underneath the sacrum (flat bony structure at the base of the spine).</p>
  <p class="abs section-head" style="left:124px;top:179px">Caution</p>
  <p class="abs section-body" style="left:124px;top:189px;width:228px">If any lower back pain is experience adjust the height the hips are elevated by using a towel or blanket that is folded to a lower height.</p>

  <p class="abs posture-label" style="left:16px;top:221px">Posture 4</p>
  <h3 class="abs serif posture-title" style="left:16px;top:232px">Supported Child’s Pose</h3>
  <div class="photo photo--wall" style="left:16px;top:258px;width:96px;height:121px;background:linear-gradient(170deg,#e6e4e1 0%,#b07a5a 45%,var(--photo-mat) 80%)" role="img" aria-label="Photo of a woman resting forward over stacked pillows in child’s pose"></div>
  <div class="photo photo--props" style="left:123px;top:258px;width:97px;height:36px" role="img" aria-label="Photo of child’s pose over a bolster"><span class="photo-tag">Props</span></div>
  <p class="abs section-head" style="left:228px;top:257px">Props</p>
  <div class="abs section-body" style="left:228px;top:267px;width:125px"><ul><li>1-2 x bolsters (or 3-4 bed pillows)</li></ul></div>
  <p class="abs section-head" style="left:124px;top:301px">Set up notes</p>
  <p class="abs section-body" style="left:124px;top:311px;width:228px">Position bolster or stacked pillows under torso. Rest the head in one direction and remember to turn to the head to the other side half way through the time you spend in this posture.</p>
  <p class="abs section-head" style="left:124px;top:348px">Caution</p>
  <p class="abs section-body" style="left:124px;top:358px;width:228px">If any knee or hip pain is experience, increase the height of the support under the torso by adding more bolsters, folded blankets or pillows.</p>

  <p class="abs posture-label" style="left:16px;top:397px">Posture 5</p>
  <h3 class="abs serif posture-title" style="left:16px;top:408px">Basic Relaxation Posture<br>with Knee Support</h3>
  <p class="abs section-head" style="left:16px;top:443px">Props</p>
  <div class="abs section-body" style="left:16px;top:453px;width:100px"><ul><li>1 x bolsters (or 1 x bed pillows or rolled up towel)</li></ul></div>
  <p class="abs section-head" style="left:16px;top:480px">Set up notes</p>
  <p class="abs section-body" style="left:16px;top:490px;width:160px">Reclining on back, position bolster or pillows under knees.</p>
  <div class="photo photo--floor" style="left:179px;top:399px;width:75px;height:105px" role="img" aria-label="Photo of a woman lying on her back with pillows under the knees"></div>
  <div class="photo photo--floor" style="left:265px;top:399px;width:75px;height:105px" role="img" aria-label="Photo of a woman lying on her back with a bolster under the knees"><span class="photo-tag">Props</span></div>
</section>

</body>
</html>
```